Business Card Design

We need a design for business cards for our company. We have a logo. We teach EMT's and we are based out of Virginia. The information that will need to add would be, name, title, phone number, email, address. On the back of the business card would be "We help you, help others"

Target Market(s)

People that want to become EMT's

Colors

Designer to choose colors to be used in the design.

Requirements
Must have
• company logo

```html
<!DOCTYPE html>
<html lang="en">
<head>
<meta charset="utf-8">
<title>Rescue Path Academy – Business Card</title>
<link rel="stylesheet" href="https://fonts.googleapis.com/css2?family=Oswald:wght@500&family=Work+Sans:wght@400;500&display=swap">
<style>
  :root {
    --backdrop: #1a1a1a;
    --card: #202020;
    --card-edge: #2a2a2a;
    --accent: #d0202e;
    --ink: #f2f2f2;
    --ink-soft: #bdbdbd;
  }
  * { margin: 0; padding: 0; box-sizing: border-box; }
  html, body { width: 1200px; height: 900px; overflow: hidden; }
  body {
    background: var(--backdrop);
    font-family: "Work Sans", Arial, sans-serif;
    color: var(--ink);
    display: flex;
    flex-direction: column;
    align-items: center;
    justify-content: center;
    gap: 40px;
  }
  .card {
    position: relative;
    width: 700px;
    height: 400px;
    background: linear-gradient(135deg, var(--card) 0%, #262626 60%, var(--card) 100%);
    border: 1px solid var(--card-edge);
    box-shadow: 0 14px 30px rgba(0,0,0,.5);
  }
  .card-front {
    display: flex;
    align-items: center;
    justify-content: center;
  }
  .brand {
    display: flex;
    align-items: center;
    gap: 14px;
  }
  .brand-dot {
    width: 22px;
    height: 22px;
    border-radius: 50%;
    background: var(--accent);
  }
  .brand-name {
    font-family: "Work Sans", Arial, sans-serif;
    font-weight: 500;
    font-size: 34px;
    letter-spacing: 1px;
    color: var(--accent);
    text-transform: uppercase;
  }
  .card-back .identity {
    position: absolute;
    left: 110px;
    top: 150px;
    width: 230px;
    text-align: right;
  }
  .person-name {
    font-family: "Oswald", Arial, sans-serif;
    font-weight: 500;
    font-size: 38px;
    letter-spacing: 1px;
    line-height: 1.1;
    color: var(--accent);
    text-transform: uppercase;
  }
  .person-title {
    font-size: 19px;
    color: var(--ink);
    margin-top: 2px;
  }
  .divider {
    position: absolute;
    left: 362px;
    top: 150px;
    width: 2px;
    height: 82px;
    background: var(--accent);
  }
  .contacts {
    position: absolute;
    left: 392px;
    top: 152px;
    list-style: none;
  }
  .contacts li {
    display: flex;
    align-items: center;
    gap: 10px;
    font-size: 19px;
    line-height: 27px;
    color: var(--ink);
  }
  .contacts svg { width: 13px; height: 13px; flex: none; }
  .address {
    position: absolute;
    left: 110px;
    bottom: 60px;
    font-size: 19px;
    color: var(--ink);
  }
</style>
</head>
<body>

  <section class="card card-front">
    <div class="brand">
      <span class="brand-dot"></span>
      <span class="brand-name">Rescue Path Academy</span>
    </div>
  </section>

  <section class="card card-back">
    <div class="identity">
      <h1 class="person-name">Daniel Harper</h1>
      <p class="person-title">Director</p>
    </div>
    <span class="divider"></span>
    <ul class="contacts">
      <li>
        <svg viewBox="0 0 16 16" aria-hidden="true"><path d="M4 1.5 6 4.5 4.6 6.2c.9 2 2.4 3.5 4.4 4.4L10.7 9.2l3 2-1 2.8C6.5 14 2 9.5 1.5 3z" fill="none" stroke="#d0202e" stroke-width="1.6" stroke-linejoin="round"/></svg>
        555-014-2286
      </li>
      <li>
        <svg viewBox="0 0 16 16" aria-hidden="true"><rect x="1.5" y="3.5" width="13" height="9" fill="none" stroke="#d0202e" stroke-width="1.5"/><path d="M1.5 3.5 8 9l6.5-5.5" fill="none" stroke="#d0202e" stroke-width="1.5"/></svg>
        hello@rescuepath.com
      </li>
      <li>
        <svg viewBox="0 0 16 16" aria-hidden="true"><circle cx="8" cy="8" r="6.5" fill="none" stroke="#d0202e" stroke-width="1.4"/><ellipse cx="8" cy="8" rx="3" ry="6.5" fill="none" stroke="#d0202e" stroke-width="1.2"/><path d="M1.5 8h13" stroke="#d0202e" stroke-width="1.2"/></svg>
        www.rescuepath.com
      </li>
    </ul>
    <p class="address">418 Linden Ave. Harrow Falls, VA 24012</p>
  </section>

</body>
</html>
```